Tidewell Electrical Solutions

On one side. LOGO (underneath:) Commercial Industrial Residential

- NAME & CONTACT DETAILS

Martin K. Oduya
Project Manager

(Cell icon) (441) 555-0187
(Email icon) twlelectricalsoultions@mailpost-demo.com
(Facebook & Instagram icons )@twlelectricalsolutions

Other side: LOGO - underneath ELECTRICAL CONSTRUCTION & MAINTENANCE . LED LIGHTING & AUTOMATION . LIFE SAFETY SYSTEMS (FIRE ALARM / SECURITY) . DATA & COMMUNICATION

```html
<!DOCTYPE html>
<html lang="en">
<head>
<meta charset="utf-8">
<title>Tidewell Electrical Solutions – Business Card</title>
<link href="https://fonts.googleapis.com/css2?family=Open+Sans:wght@400;600;700&family=Raleway:wght@600&display=swap" rel="stylesheet">
<style>
  :root {
    --teal: #0e5266;
    --teal-line: #6f9aa8;
    --ink: #3a3a3a;
    --paper: #ffffff;
    --backdrop: #dcdcdc;
  }
  * { margin: 0; padding: 0; box-sizing: border-box; }
  html, body {
    width: 1200px; height: 802px; overflow: hidden;
    background: var(--backdrop);
    font-family: "Open Sans", sans-serif;
  }
  .canvas { position: relative; width: 1200px; height: 802px; }

  .card {
    position: absolute; top: 274px;
    width: 443px; height: 265px;
    box-shadow: 2px 3px 6px rgba(0,0,0,.35);
    overflow: hidden;
  }
  .card--front { left: 136px; background: var(--paper); }
  .card--back  { left: 624px; background: var(--teal); }

  /* front: brand */
  .brand {
    position: absolute; left: 17px; top: 112px;
    display: flex; align-items: center; gap: 9px;
  }
  .brand__square { width: 22px; height: 22px; background: var(--teal); }
  .brand__name {
    color: var(--teal); font-weight: 600;
    font-size: 10px; line-height: 11.5px; letter-spacing: 1.6px;
    text-transform: uppercase;
  }

  .divider {
    position: absolute; left: 178px; top: 75px;
    width: 1px; height: 120px; background: var(--teal-line);
  }

  .person { position: absolute; left: 190px; top: 72px; }
  .person__name {
    font-family: "Raleway", sans-serif; font-weight: 600;
    font-size: 16.5px; color: var(--teal); letter-spacing: .1px;
  }
  .person__title { font-size: 11.5px; color: var(--ink); margin-left: 3px; margin-top: -1px; }

  .contacts { position: absolute; left: 190px; top: 117px; list-style: none; }
  .contact {
    display: flex; align-items: center; gap: 5px;
    height: 21px; font-size: 11px; color: var(--ink);
  }
  .contact--email { font-size: 9.6px; }
  .contact__icon { width: 15px; height: 15px; flex: none; }

  .sectors {
    position: absolute; left: 0; bottom: 0; width: 100%; height: 38px;
    background: var(--teal); color: #fff;
    display: flex; align-items: center; justify-content: center;
    font-size: 11.5px; letter-spacing: .1px;
  }

  /* back: services */
  .services {
    position: absolute; left: 0; top: 92px; width: 100%;
    list-style: none; text-align: center; color: #fff;
    font-weight: 600; font-size: 11.5px; line-height: 21px;
    text-transform: uppercase;
  }
</style>
</head>
<body>
<main class="canvas">

  <section class="card card--front" aria-label="Card front">
    <div class="brand">
      <span class="brand__square"></span>
      <span class="brand__name">Tidewell<br>Electrical<br>Solutions</span>
    </div>

    <span class="divider"></span>

    <div class="person">
      <h1 class="person__name">MARTIN K. ODUYA</h1>
      <p class="person__title">Project Manager</p>
    </div>

    <ul class="contacts">
      <li class="contact">
        <svg class="contact__icon" viewBox="0 0 16 16" aria-hidden="true">
          <circle cx="8" cy="8" r="7.2" fill="none" stroke="#0e5266" stroke-width="1"/>
          <rect x="5.5" y="3.8" width="5" height="8.4" rx="1" fill="none" stroke="#0e5266" stroke-width="1"/>
          <line x1="7.3" y1="10.9" x2="8.7" y2="10.9" stroke="#0e5266" stroke-width="0.8"/>
        </svg>
        <span>(441) 555-0187</span>
      </li>
      <li class="contact contact--email">
        <svg class="contact__icon" viewBox="0 0 16 16" aria-hidden="true">
          <circle cx="8" cy="8" r="7.2" fill="#0e5266"/>
          <rect x="4" y="5.2" width="8" height="5.6" fill="#fff"/>
          <polyline points="4,5.4 8,8.6 12,5.4" fill="none" stroke="#0e5266" stroke-width="0.9"/>
        </svg>
        <span>twlelectricalsoultions@mailpost-demo.com</span>
      </li>
      <li class="contact">
        <svg class="contact__icon" viewBox="0 0 16 16" aria-hidden="true">
          <circle cx="8" cy="8" r="7.2" fill="none" stroke="#0e5266" stroke-width="1"/>
        </svg>
        <span>@twlelectricalsolutions</span>
      </li>
      <li class="contact">
        <svg class="contact__icon" viewBox="0 0 16 16" aria-hidden="true">
          <circle cx="8" cy="8" r="7.2" fill="none" stroke="#0e5266" stroke-width="1"/>
        </svg>
        <span>@twlelectricalsolutions</span>
      </li>
    </ul>

    <p class="sectors">COMMERCIAL INDUSTRIAL RESIDENTIAL</p>
  </section>

  <section class="card card--back" aria-label="Card back">
    <ul class="services">
      <li>Electrical Construction &amp; Maintenance</li>
      <li>LED Lighting &amp; Automation</li>
      <li>Life Safety Systems (Fire Alarm / Security)</li>
      <li>Data &amp; Communication</li>
    </ul>
  </section>

</main>
</body>
</html>
```